Shampoo and Shower Gel Packaging Design

I need a new packaging design for a men shampoo and shower gel bottle. The packaging must me black (black bottle/package) and the logo should be also monochrom.
For example, black matte bottle and black shiny logo on the packaging (not mandatory).
the design must contain maximum 3 colors.
1. black
2. white (text)
3. grey/dark blue/dark green (colors will be the difference between products parfumes/smell/scences.

Design must be minimalist/elegant/discrete.
Updates

Please check the photos i added for pure inspiration.

Target Market(s)

brand exclusively for MEN - premium clients

Industry/Entity Type

Cosmetics

Font styles to use
Sans Serif

Colors
1b1b1b
5c5c5c
aaaaaa
ffffff
3176b5

Requirements
Must have
• black background
• minimalist design

```html
<!DOCTYPE html>
<html lang="en">
<head>
<meta charset="utf-8">
<title>Orvane Cosmetics – Shampoo Label</title>
<link rel="stylesheet" href="https://fonts.googleapis.com/css2?family=Raleway:wght@200;300&family=Open+Sans:wght@400&display=swap">
<style>
  :root {
    --label-black: #0b0b0b;
    --ink-white: #ffffff;
    --ink-soft: #d8d8d8;
    --rule-grey: #8a8a8a;
  }
  * { margin: 0; padding: 0; box-sizing: border-box; }
  html, body {
    width: 1200px;
    height: 1200px;
    overflow: hidden;
    background: var(--label-black);
  }
  .label {
    position: relative;
    width: 1200px;
    height: 1200px;
    background: var(--label-black);
    color: var(--ink-white);
    font-family: 'Raleway', sans-serif;
    text-align: center;
  }
  .brand {
    position: absolute;
    top: 380px;
    left: 0;
    width: 100%;
    font-weight: 300;
    color: var(--ink-white);
  }
  .brand-name {
    display: block;
    font-size: 92px;
    letter-spacing: 0.38em;
    padding-left: 0.38em;
    line-height: 1;
  }
  .brand-sub {
    display: block;
    margin-top: 18px;
    font-size: 20px;
    letter-spacing: 0.6em;
    padding-left: 0.6em;
  }
  .product {
    position: absolute;
    top: 610px;
    left: 50%;
    transform: translateX(-50%);
    width: 460px;
  }
  .product-type {
    font-weight: 300;
    font-size: 62px;
    color: var(--ink-soft);
    letter-spacing: 0.01em;
    line-height: 1;
    padding-bottom: 22px;
  }
  .product-claim {
    border-top: 1px solid var(--rule-grey);
    border-bottom: 1px solid var(--rule-grey);
    padding: 26px 0;
    font-family: 'Open Sans', sans-serif;
    font-size: 22px;
    color: var(--ink-soft);
  }
  .volume {
    position: absolute;
    top: 930px;
    left: 0;
    width: 100%;
    font-family: 'Open Sans', sans-serif;
    font-size: 22px;
    color: var(--ink-soft);
  }
</style>
</head>
<body>
  <main class="label">
    <h1 class="brand">
      <span class="brand-name">ORVANE</span>
      <span class="brand-sub">COSMETICS</span>
    </h1>
    <section class="product">
      <h2 class="product-type">Shampoo</h2>
      <p class="product-claim">Advance Hair Fall Control</p>
    </section>
    <p class="volume">200ml</p>
  </main>
</body>
</html>
```